Business Card for Language School (2 locations)

We need a sleek business card for a language school that is looking to update our image to be more professional. We work with students ages Pre-Kindergarten through adults. Our idea is to have an all-black business card with white or silver lettering. On the front will be the name of our school (Bright Meadow English Academy), and on the back there will be information for our location, phone number, email, and website (and possibly social media information). We have two school branches, so the address, phone number, and email address will be different for each branch, but all of the other information will stay the same. We'd like each branch to have a different color card edge that is neon. We are also open to suggestions and new ideas!

Some answers to questions we have received:
1. The reason we haven't added a logo is because we are looking to get a new one. We hadn't originally planned to do that at this time, but we are going to look into updating our project to include that as another aspect of it. We had previously planned to just include the school name on the front without a logo at this time.
2. We currently have two branches of our school, and we want our business card design to be uniform for each location. While it might make sense to put the information on one card right now, we plan to have more locations in the future, so we want to plan ahead with a unified design right now.
3. Our school addresses and phone numbers can be found on our website: www.brightmeadowlingo.example (at the bottom of the page)!
Updates

Part of this contest is also a new logo design. Our previous design was a train, which we would be open to keeping if it had an updated, sleeker design.

Contact Information for Business Card

Card #1:
Bright Meadow English Academy (Qinglu Branch)
Fuxing W. Rd. Sec. 3, Lane 412, No. 58, 1F
Beitou District, Taipei City 11260
02-2941-3086
qinglu@brightmeadowlingo.example

Card #2:
Bright Meadow English Academy (Heping Branch)
Linsen Road, No. 318, 1F
Songshan District, Taipei City 10587
02-2764-1520
heping@brightmeadowlingo.example

Both cards:
Website: www.brightmeadowlingo.example
Facebook: www.facebook.com/brightmeadowlingo
Instagram: @brightmeadowlingo

```html
<!DOCTYPE html>
<html lang="en">
<head>
<meta charset="utf-8">
<title>Bright Meadow English Academy – Business Cards</title>
<link rel="stylesheet" href="https://fonts.googleapis.com/css2?family=Mulish:wght@600;800&display=swap">
<style>
  :root {
    --canvas: #ffffff;
    --card-black: #141312;
    --card-mid: #2a2725;
    --ink: #ffffff;
    --ink-muted: #9a9694;
    --letters-tone: rgba(150, 146, 142, 0.22);
    --tab-grey: #58555a;
  }
  * { box-sizing: border-box; margin: 0; padding: 0; }
  html, body {
    width: 1200px; height: 1200px; overflow: hidden;
    background: var(--canvas);
    font-family: "Mulish", "Century Gothic", sans-serif;
  }
  .sheet { position: relative; width: 1200px; height: 1200px; }

  .card {
    position: absolute;
    width: 579px; height: 355px;
    overflow: hidden;
    color: var(--ink);
  }
  .card--front {
    top: 230px;
    background: linear-gradient(180deg, var(--card-black) 0%, var(--card-mid) 32%, var(--card-mid) 52%, var(--card-black) 78%, var(--card-black) 100%);
  }
  .card--back {
    top: 614px;
    background: linear-gradient(180deg, var(--card-black) 0%, var(--card-mid) 18%, #232120 55%, var(--card-black) 100%);
  }
  .card--qinglu { left: 0; }
  .card--heping { left: 622px; }

  .letters-field {
    position: absolute; left: 0; right: 0;
  }
  .card--front .letters-field {
    bottom: 0; height: 110px;
    background: linear-gradient(180deg, transparent 0%, var(--letters-tone) 55%, transparent 100%);
  }
  .card--back .letters-field {
    top: 0; height: 110px;
    background: linear-gradient(180deg, transparent 0%, var(--letters-tone) 45%, transparent 100%);
  }

  .wordmark {
    position: absolute; left: 0; right: 0; top: 108px;
    text-align: center;
  }
  .wordmark__name {
    display: block;
    font-weight: 800;
    font-size: 50px;
    line-height: 1;
    letter-spacing: -0.5px;
    color: var(--ink);
  }
  .wordmark__branch {
    display: block;
    margin-top: 8px;
    font-weight: 600;
    font-size: 13px;
    letter-spacing: 0.5px;
    color: var(--ink-muted);
  }
  .wordmark__sub {
    display: flex; justify-content: center; align-items: center; gap: 12px;
    margin-top: 10px;
    font-weight: 800;
    font-size: 24px;
    color: var(--ink);
  }
  .wordmark__dot {
    width: 10px; height: 10px; border-radius: 50%; background: var(--ink);
  }

  .contact {
    position: absolute; left: 28px; top: 158px;
    font-weight: 800;
    font-size: 15.5px;
    line-height: 22px;
    letter-spacing: 0.3px;
  }
  .contact__row { display: flex; white-space: nowrap; }
  .contact__label--wide { width: 72px; }
  .contact__label--web { width: 95px; }
  .contact__rule {
    width: 408px; height: 0;
    border-top: 1.5px dashed var(--ink);
    margin: 8px 0 7px;
  }
  .card__tab {
    position: absolute; left: 28px; bottom: 0;
    width: 92px; height: 5px; background: var(--tab-grey);
  }
</style>
</head>
<body>
<main class="sheet">

  <section class="card card--front card--qinglu">
    <div class="letters-field" role="img" aria-label="Scattered alphabet letters decoration"></div>
    <h1 class="wordmark">
      <span class="wordmark__name">BRIGHT MEADOW</span>
      <span class="wordmark__branch">(QINGLU BRANCH)</span>
      <span class="wordmark__sub"><span>English</span><span class="wordmark__dot"></span><span>Academy</span></span>
    </h1>
  </section>

  <section class="card card--front card--heping">
    <div class="letters-field" role="img" aria-label="Scattered alphabet letters decoration"></div>
    <h1 class="wordmark">
      <span class="wordmark__name">BRIGHT MEADOW</span>
      <span class="wordmark__branch">(HEPING BRANCH)</span>
      <span class="wordmark__sub"><span>English</span><span class="wordmark__dot"></span><span>Academy</span></span>
    </h1>
  </section>

  <section class="card card--back card--qinglu">
    <div class="letters-field" role="img" aria-label="Scattered alphabet letters decoration"></div>
    <div class="contact">
      <div class="contact__row">Fuxing W. Rd. Sec. 3, Lane 412, No. 58, 1F</div>
      <div class="contact__row">Beitou District, Taipei City 11260</div>
      <div class="contact__row"><span class="contact__label--wide">Phone:</span>02-2941-3086</div>
      <div class="contact__row"><span>Email:&nbsp;</span>qinglu@brightmeadowlingo.example</div>
      <div class="contact__rule"></div>
      <div class="contact__row"><span class="contact__label--web">Website:</span>www.brightmeadowlingo.example</div>
      <div class="contact__row"><span class="contact__label--web">Facebook:</span>www.facebook.com/brightmeadowlingo</div>
      <div class="contact__row"><span>Instagram:&nbsp;</span>@brightmeadowlingo</div>
    </div>
    <div class="card__tab"></div>
  </section>

  <section class="card card--back card--heping">
    <div class="letters-field" role="img" aria-label="Scattered alphabet letters decoration"></div>
    <div class="contact">
      <div class="contact__row">Linsen Road, No. 318, 1F</div>
      <div class="contact__row">Songshan District, Taipei City 10587</div>
      <div class="contact__row"><span class="contact__label--wide">Phone:</span>02-2764-1520</div>
      <div class="contact__row"><span>Email:&nbsp;</span>heping@brightmeadowlingo.example</div>
      <div class="contact__rule"></div>
      <div class="contact__row"><span class="contact__label--web">Website:</span>www.brightmeadowlingo.example</div>
      <div class="contact__row"><span class="contact__label--web">Facebook:</span>www.facebook.com/brightmeadowlingo</div>
      <div class="contact__row"><span>Instagram:&nbsp;</span>@brightmeadowlingo</div>
    </div>
    <div class="card__tab"></div>
  </section>

</main>
</body>
</html>
```